Willow Ridge Coffee Company Label

I am in need of a label for my coffee brand. I've attached my logo, and the label I've composed in the past. This brand has not launched yet, but we will launch within the week. I'm trying to identify other label options. I am familiar with Adobe Illustrator, enough to design what I have. What I'd like is a logo that is scalable, meaning I can easily change the name of the coffee. For consistency I'd like all of my roasts to have the same label, just different names and descriptions. I've included specs for the label, I'll be using the 3x4 labels for 16 oz bags. When you submit your design please follow the specs. There needs to be my company name and address on the label, however I don't want it to take over the label.

Please reply with any questions or clarifications.

Thank you,

Ned

```html
<!DOCTYPE html>
<html lang="en">
<head>
<meta charset="utf-8">
<title>Willow Ridge Coffee Co. – Long Haul Blend Label</title>
<link href="https://fonts.googleapis.com/css2?family=Noto+Serif:ital,wght@0,400;1,400&family=Open+Sans:wght@400&display=swap" rel="stylesheet">
<style>
  :root {
    --backdrop: #2e0000;
    --roast: #56321a;
    --label-top: #7d5e4c;
    --label-mid: #b3a297;
    --label-base: #dedcdd;
    --cream: #ffffff;
    --caramel: #b47a2c;
    --bean: #6e4a3c;
  }
  * { margin: 0; padding: 0; box-sizing: border-box; }
  html, body {
    width: 1200px; height: 1200px; overflow: hidden;
    background: var(--backdrop);
  }
  .stage {
    width: 1200px; height: 1200px;
    display: flex; align-items: center; justify-content: center;
  }
  .label {
    position: relative;
    width: 600px; height: 1000px;
    background: linear-gradient(168deg, var(--label-top) 0%, var(--label-mid) 38%, var(--label-base) 70%, var(--label-base) 100%);
    overflow: hidden;
    box-shadow: 0 4px 10px rgba(0,0,0,0.35);
  }
  .brand {
    position: absolute; top: 60px; left: 0; right: 0;
    display: flex; flex-direction: column; align-items: center;
  }
  .brand-mark {
    width: 120px; height: 120px; border-radius: 50%;
    background: var(--roast);
    margin-bottom: 42px;
  }
  .brand-name {
    font-family: "Noto Serif", serif;
    font-weight: 400;
    color: var(--roast);
    font-size: 36px;
    line-height: 1.1;
    text-align: center;
    letter-spacing: 1px;
  }
  .blend-band {
    position: absolute; top: 327px; left: 0; right: 0; height: 67px;
    background: var(--roast);
    display: flex; align-items: center; justify-content: center;
  }
  .blend-name {
    font-family: "Noto Serif", serif;
    font-weight: 400;
    font-variant: small-caps;
    font-size: 40px;
    line-height: 1;
    color: var(--cream);
    letter-spacing: 1.5px;
  }
  .tagline {
    position: absolute; top: 406px; left: 0; right: 0;
    font-family: "Noto Serif", serif;
    font-style: italic;
    font-size: 22px;
    line-height: 26px;
    color: var(--roast);
    text-align: center;
  }
  .flavor-notes {
    position: absolute; top: 515px; left: 159px;
    font-family: "Open Sans", sans-serif;
    color: var(--roast);
    list-style: none;
  }
  .flavor-notes li {
    font-size: 28px;
    line-height: 46px;
    text-transform: uppercase;
    letter-spacing: -0.5px;
  }
  .flavor-notes .initial { font-size: 42px; }
  .road-art {
    position: absolute; left: 80px; right: 80px; top: 718px; bottom: 0;
    border-radius: 200px 200px 0 0;
    background: linear-gradient(180deg, var(--bean) 0%, var(--roast) 60%, var(--caramel) 100%);
    opacity: 0.9;
  }
</style>
</head>
<body>
  <main class="stage">
    <section class="label">
      <header class="brand">
        <div class="brand-mark"></div>
        <p class="brand-name">Willow Ridge<br>Coffee Co.</p>
      </header>

      <div class="blend-band">
        <h1 class="blend-name">Long Haul Blend</h1>
      </div>

      <p class="tagline">Perfect for use as an espresso, or on it’s own.<br>Compliments your daily commute or road trip</p>

      <ul class="flavor-notes">
        <li><span class="initial">B</span>alanced,</li>
        <li><span class="initial">C</span>armelly&nbsp; sweet</li>
        <li><span class="initial">E</span>spresso strength</li>
      </ul>

      <div class="road-art" role="img" aria-label="Illustration of a winding brown road with a yellow centre line curling around scattered coffee beans"></div>
    </section>
  </main>
</body>
</html>
```